Web App Dashboard Design for a Smart Home

We are a company that gives consultancy and installation services for custom smart home designs to household owners in ON, Canada. For our web application, we are in need of a dashboard design which will display multiple rooms that could be present in a home. This should be a flexible design as the number of rooms where smart devices installed will vary from house to house. We would like to see the name of the rooms and several icons that represent different monitored objects in each room like temperature, light on/off, sound/music on/off, humidity, illuminance, noise level, air quality, for bathrooms and kitchens wet/dry conditions, windows/doors open, curtains open/closed etc. The web application will collect the latest status data from all related sensors and it will be publishing the latest status for each room into this dashboard. Backend of the dashboards should contain nice modern looking houses and it would be good if there are multiple versions of the background pictures that rotate.

Target Market(s)

Mid-Market range house holders who want to increase their comfort and safety with smart home implementations

Industry/Entity Type

Small Business

Number of Pages Required

1 page

Colors
0455a3
3277b5
85acd3
86cae7
fbf289
cadf82
acd037
9bcb3c
faa54b

Requirements
Must have
• - A Flexible Dashboard Design which can hold many rooms but still look sharp even with only 1/2 rooms as well.
• - An smart home icon library that will show the monitored value like temperature, lights on/off, door/window open/close etc.

```html
<!DOCTYPE html>
<html lang="en">
<head>
<meta charset="utf-8">
<title>Smart Home Dashboard</title>
<link href="https://fonts.googleapis.com/css2?family=Roboto:wght@400;500&display=swap" rel="stylesheet">
<style>
  :root {
    --sidebar: #1b4f8f;
    --page: #e9e9e9;
    --card: #ffffff;
    --brand: #0455a3;
    --text: #333333;
    --toggle-off: #e6e6e6;
    --toggle-on: #4cd964;
    --white: #ffffff;
  }
  * { box-sizing: border-box; margin: 0; padding: 0; }
  html, body { width: 1200px; height: 850px; overflow: hidden; }
  body {
    position: relative;
    background: var(--page);
    font-family: "Roboto", Arial, sans-serif;
    color: var(--text);
  }
  .sidebar {
    position: absolute; left: 0; top: 0;
    width: 105px; height: 850px;
    background: var(--sidebar);
  }
  .nav-item {
    position: absolute; left: 0; width: 105px;
    display: flex; flex-direction: column; align-items: center;
    color: var(--white); font-size: 11.5px;
  }
  .nav-item svg { width: 30px; height: 28px; margin-bottom: 3px; fill: var(--white); }
  .page-header { position: absolute; left: 208px; top: 38px; }
  .page-title { font-size: 22px; font-weight: 500; color: var(--brand); line-height: 1.1; }
  .page-subtitle { font-size: 12px; color: #222; margin-top: 1px; }
  .card {
    position: absolute;
    background: var(--card);
    padding: 17px 22px 0 19px;
  }
  .card-title { font-size: 13px; font-weight: 500; color: var(--brand); margin-bottom: 15px; }
  .status-row {
    display: flex; align-items: center;
    height: 21.5px; font-size: 12.8px;
  }
  .card.roomy .status-row { height: 23.5px; }
  .status-row .icon { width: 14px; height: 14px; fill: var(--brand); margin-right: 12px; flex: none; }
  .status-row .label { flex: 1; }
  .toggle {
    width: 32px; height: 18px; border-radius: 9px;
    background: var(--toggle-off); position: relative; flex: none;
  }
  .toggle::after {
    content: ""; position: absolute; top: 2px; left: 2px;
    width: 14px; height: 14px; border-radius: 50%; background: var(--white);
    box-shadow: 0 1px 2px rgba(0,0,0,.15);
  }
  .toggle.on { background: var(--toggle-on); }
  .toggle.on::after { left: 16px; }
  .camera-feed {
    position: absolute; left: 18px; top: 43px; width: 546px; height: 307px;
    background: radial-gradient(ellipse at 50% 45%, #c9cfd6 0%, #8d8a86 45%, #3c4a52 75%, #0c0c0c 100%);
  }
</style>
</head>
<body>
<svg width="0" height="0" style="position:absolute">
  <symbol id="i-bulb" viewBox="0 0 16 16"><path d="M8 1a5 5 0 0 0-3 9c.6.5 1 1.2 1 2h4c0-.8.4-1.5 1-2a5 5 0 0 0-3-9z"/><rect x="6" y="13" width="4" height="1.5" rx=".5"/></symbol>
  <symbol id="i-thermo" viewBox="0 0 16 16"><path d="M8 1a2 2 0 0 0-2 2v6.5a3.5 3.5 0 1 0 4 0V3a2 2 0 0 0-2-2zm0 1.5a.5.5 0 0 1 .5.5v7.3l.4.3a2 2 0 1 1-1.8 0l.4-.3V3a.5.5 0 0 1 .5-.5z"/><circle cx="8" cy="12.5" r="1.3"/></symbol>
  <symbol id="i-speaker" viewBox="0 0 16 16"><path d="M1 6h3l4-3v10L4 10H1z"/><path d="M10 5.5a3 3 0 0 1 0 5M12 3.5a6 6 0 0 1 0 9" stroke="currentColor" fill="none" stroke-width="1.4" style="stroke:var(--brand)"/></symbol>
  <symbol id="i-wind" viewBox="0 0 16 16"><path d="M1 5h9a2 2 0 1 0-2-2M1 8h12a2 2 0 1 1-2 2M1 11h6" fill="none" stroke-width="1.5" style="stroke:var(--brand)"/></symbol>
  <symbol id="i-door" viewBox="0 0 16 16"><path d="M4 1h8v13H4z"/><rect x="1" y="14" width="14" height="1.5"/><circle cx="10" cy="8" r=".9" fill="#fff"/></symbol>
  <symbol id="i-lamp" viewBox="0 0 16 16"><path d="M4 1h8l2 6H2z"/><rect x="7" y="7" width="2" height="5"/><rect x="4" y="12" width="8" height="3" rx="1"/></symbol>
  <symbol id="i-drop" viewBox="0 0 16 16"><path d="M8 1s-5 6-5 9a5 5 0 0 0 10 0c0-3-5-9-5-9z"/><path d="M6 12l4-4M6.3 8.5h.1M9.6 11.6h.1" stroke="#fff" stroke-width="1.2"/></symbol>
  <symbol id="i-clock" viewBox="0 0 16 16"><circle cx="8" cy="8" r="7"/><path d="M8 4v4.5l3 1.5" stroke="#fff" stroke-width="1.5" fill="none"/></symbol>
  <symbol id="i-outside" viewBox="0 0 16 16"><path d="M5 1a2 2 0 0 0-2 2v6.5a3.5 3.5 0 1 0 4 0V3a2 2 0 0 0-2-2zm0 1.5a.5.5 0 0 1 .5.5v7.3l.4.3a2 2 0 1 1-1.8 0l.4-.3V3a.5.5 0 0 1 .5-.5z"/><circle cx="12.5" cy="3" r="1.7" fill="none" stroke-width="1.2" style="stroke:var(--brand)"/></symbol>
</svg>

<nav class="sidebar">
  <div class="nav-item" style="top:33px">
    <svg viewBox="0 0 24 24"><path d="M12 3 2 11h3v9h5v-6h4v6h5v-9h3z"/></svg>Dashboard
  </div>
  <div class="nav-item" style="top:104px">
    <svg viewBox="0 0 24 24"><path d="M3 21V13h3v8zm5 0V9h3v12zm5 0v-6h3v6zm5 0V8h3v13zM3 9l5-5 5 5 7-6" stroke="#fff" stroke-width="0"/><path d="M3 10l5-4.5 5 4 7-6.5" fill="none" stroke="#fff" stroke-width="2"/></svg>Usage
  </div>
  <div class="nav-item" style="top:176px">
    <svg viewBox="0 0 24 24"><path d="M12 2a1.5 1.5 0 0 0-1.5 1.5v.7A6 6 0 0 0 6 10v5l-2 3h16l-2-3v-5a6 6 0 0 0-4.5-5.8v-.7A1.5 1.5 0 0 0 12 2zm-2 18a2 2 0 0 0 4 0z"/></svg>Notifications
  </div>
  <div class="nav-item" style="top:248px">
    <svg viewBox="0 0 24 24"><path d="M10 2h4l.5 3 2 1 2.6-1.6 2.8 2.8L20.3 9.8l.7 2.2 3 .5v4l-3 .5-.7 2-0 0 1.6 2.6-2.8 2.8-2.6-1.6-2 .9-.5 3h-4l-.5-3-2-.9-2.6 1.6-2.8-2.8 1.6-2.6-.8-2-3-.5v-4l3-.5.8-2.2L2.1 7.2l2.8-2.8L7.5 6l2-1zM12 9a3 3 0 1 0 0 6 3 3 0 0 0 0-6z" transform="scale(.9) translate(1.3 0)"/></svg>Configuration
  </div>
  <div class="nav-item" style="top:749px">
    <svg viewBox="0 0 24 24"><path d="M4 4h7v2.5H6.5v11H11V20H4zM14 7l5 5-5 5v-3.2H9v-3.6h5z"/></svg>Logout
  </div>
</nav>

<header class="page-header">
  <h1 class="page-title">Dashboard</h1>
  <p class="page-subtitle">Here you can control every aspect of your house, for each room individually</p>
</header>

<section class="card" style="left:206px;top:99px;width:282px;height:175px">
  <h2 class="card-title">Main entrance</h2>
  <div class="status-row"><svg class="icon"><use href="#i-outside"/></svg><span class="label">58°F outside</span></div>
  <div class="status-row"><svg class="icon"><use href="#i-bulb"/></svg><span class="label">Porch light</span><span class="toggle"></span></div>
  <div class="status-row"><svg class="icon"><use href="#i-speaker"/></svg><span class="label">High noise levels</span></div>
  <div class="status-row"><svg class="icon"><use href="#i-wind"/></svg><span class="label">Windy</span></div>
  <div class="status-row"><svg class="icon"><use href="#i-door"/></svg><span class="label">Entrance door</span><span class="toggle on"></span></div>
</section>

<section class="card roomy" style="left:206px;top:284px;width:282px;height:181px">
  <h2 class="card-title">Master bedroom</h2>
  <div class="status-row"><svg class="icon"><use href="#i-bulb"/></svg><span class="label">Ceiling light 1</span><span class="toggle"></span></div>
  <div class="status-row"><svg class="icon"><use href="#i-bulb"/></svg><span class="label">Ceiling light 2</span><span class="toggle on"></span></div>
  <div class="status-row"><svg class="icon"><use href="#i-lamp"/></svg><span class="label">Lamp</span><span class="toggle on"></span></div>
  <div class="status-row"><svg class="icon"><use href="#i-thermo"/></svg><span class="label">95°F</span></div>
  <div class="status-row"><svg class="icon"><use href="#i-drop"/></svg><span class="label">Low humidity</span></div>
</section>

<section class="card roomy" style="left:206px;top:474px;width:282px;height:181px">
  <h2 class="card-title">Kids bedroom</h2>
  <div class="status-row"><svg class="icon"><use href="#i-bulb"/></svg><span class="label">Ceiling light 1</span><span class="toggle"></span></div>
  <div class="status-row"><svg class="icon"><use href="#i-lamp"/></svg><span class="label">Lamp</span><span class="toggle on"></span></div>
  <div class="status-row"><svg class="icon"><use href="#i-lamp"/></svg><span class="label">Lamp 2</span><span class="toggle on"></span></div>
  <div class="status-row"><svg class="icon"><use href="#i-thermo"/></svg><span class="label">95°F</span></div>
  <div class="status-row"><svg class="icon"><use href="#i-drop"/></svg><span class="label">Low humidity</span></div>
</section>

<section class="card roomy" style="left:207px;top:668px;width:282px;height:137px">
  <h2 class="card-title">Kids bathroom</h2>
  <div class="status-row"><svg class="icon"><use href="#i-bulb"/></svg><span class="label">Ceiling light</span><span class="toggle"></span></div>
  <div class="status-row"><svg class="icon"><use href="#i-thermo"/></svg><span class="label">50°F</span></div>
  <div class="status-row"><svg class="icon"><use href="#i-clock"/></svg><span class="label">Busy</span></div>
</section>

<section class="card roomy" style="left:505px;top:99px;width:281px;height:181px">
  <h2 class="card-title">Living room</h2>
  <div class="status-row"><svg class="icon"><use href="#i-bulb"/></svg><span class="label">Ceiling light 1</span><span class="toggle"></span></div>
  <div class="status-row"><svg class="icon"><use href="#i-bulb"/></svg><span class="label">Ceiling light 2</span><span class="toggle on"></span></div>
  <div class="status-row"><svg class="icon"><use href="#i-lamp"/></svg><span class="label">Lamp</span><span class="toggle on"></span></div>
  <div class="status-row"><svg class="icon"><use href="#i-thermo"/></svg><span class="label">95°F</span></div>
  <div class="status-row"><svg class="icon"><use href="#i-drop"/></svg><span class="label">Low humidity</span></div>
</section>

<section class="card roomy" style="left:505px;top:290px;width:281px;height:132px">
  <h2 class="card-title">Master bedroom bathroom</h2>
  <div class="status-row"><svg class="icon"><use href="#i-bulb"/></svg><span class="label">Ceiling light</span><span class="toggle"></span></div>
  <div class="status-row"><svg class="icon"><use href="#i-thermo"/></svg><span class="label">50°F</span></div>
  <div class="status-row"><svg class="icon"><use href="#i-clock"/></svg><span class="label">Busy</span></div>
</section>

<section class="card roomy" style="left:804px;top:99px;width:281px;height:132px">
  <h2 class="card-title">Guest bathroom</h2>
  <div class="status-row"><svg class="icon"><use href="#i-bulb"/></svg><span class="label">Ceiling light</span><span class="toggle"></span></div>
  <div class="status-row"><svg class="icon"><use href="#i-thermo"/></svg><span class="label">50°F</span></div>
  <div class="status-row"><svg class="icon"><use href="#i-clock"/></svg><span class="label">Busy</span></div>
</section>

<section class="card" style="left:804px;top:242px;width:281px;height:180px">
  <h2 class="card-title">Back entrance</h2>
  <div class="status-row"><svg class="icon"><use href="#i-outside"/></svg><span class="label">58°F outside</span></div>
  <div class="status-row"><svg class="icon"><use href="#i-bulb"/></svg><span class="label">Porch light</span><span class="toggle"></span></div>
  <div class="status-row"><svg class="icon"><use href="#i-speaker"/></svg><span class="label">High noise levels</span></div>
  <div class="status-row"><svg class="icon"><use href="#i-wind"/></svg><span class="label">Windy</span></div>
  <div class="status-row"><svg class="icon"><use href="#i-door"/></svg><span class="label">Entrance door</span><span class="toggle on"></span></div>
</section>

<section class="card" style="left:505px;top:433px;width:580px;height:375px">
  <h2 class="card-title">Front door camera</h2>
  <div class="camera-feed" role="img" aria-label="Live wide-angle front door camera view of the driveway, parked cars and houses across the street"></div>
</section>
</body>
</html>
```